Stonevale Business Card Design

The Stonevale Co is an aggregate (crushing) equipment dealer serving Western Canadian provinces. Stonevale is a distributor of aggregate equipment for different manufacturers.

We are looking to change and update the existing business card which has been used since the existence of the company. A copy of existing card has been attached for reference. The Stonevale Co logo we want to remain the same and we want the green color to remain the same.

We are wanting something new with a different look. A refreshing card to show a new modern and updated look. No longer wanting to have the manufacturers on the back of the card but something more like our logo on the back of the card with a statement like "Crushing Solutions"

ideas could be:
- card can be different colors on front and back
- front or reverse of the card could possibly be the green color with the logo in black

Target Market(s)

Owners of Aggregate/Crushing companies

Contact Information for Business Card

see above

Requirements
Must have
• - logo to remain same along with same font within logo
• - green color to remain same
Nice to have
• as noted above under project description
Should not have

```html
<!DOCTYPE html>
<html lang="en">
<head>
<meta charset="utf-8">
<title>Stonevale Co Business Card</title>
<link href="https://fonts.googleapis.com/css2?family=Open+Sans:wght@400;600;700&display=swap" rel="stylesheet">
<style>
  :root {
    --olive: #8a8a14;
    --olive-light: #9a9a1c;
    --olive-dark: #4d5418;
    --ink: #1e1e1e;
    --paper: #ffffff;
    --backdrop: #e4e5e7;
    --rule: #555555;
  }
  * { margin: 0; padding: 0; box-sizing: border-box; }
  html, body { width: 1200px; height: 1200px; overflow: hidden; }
  body {
    background: var(--backdrop);
    font-family: "Open Sans", Arial, sans-serif;
    color: var(--ink);
    position: relative;
  }
  .card {
    position: absolute;
    left: 160px;
    width: 880px;
    height: 503px;
    overflow: hidden;
    box-shadow: 0 6px 18px rgba(0,0,0,0.12);
  }
  .card-front { top: 70px; background: var(--paper); }
  .card-back {
    top: 627px;
    background: linear-gradient(160deg, var(--olive) 0%, #6b7016 50%, var(--olive-dark) 100%);
  }

  /* Front */
  .brand { position: absolute; left: 64px; top: 70px; }
  .brand-name {
    font-weight: 700;
    font-size: 34px;
    letter-spacing: 0.5px;
    color: var(--olive);
  }
  .brand-tagline {
    margin-top: 6px;
    font-weight: 400;
    font-size: 19px;
    letter-spacing: 0.3px;
    color: var(--ink);
  }
  .front-rule {
    position: absolute; left: 64px; top: 190px;
    width: 440px; height: 1px; background: var(--rule);
  }
  .address {
    position: absolute; left: 64px; top: 250px;
    display: flex; gap: 12px; align-items: flex-start;
    font-size: 18px; line-height: 1.45;
  }
  .band {
    position: absolute; left: 0; bottom: 0;
    width: 100%; height: 150px;
    background: linear-gradient(90deg, var(--olive) 0%, var(--olive-light) 100%);
  }
  .contact {
    position: absolute; right: 56px; top: 222px;
    text-align: right;
  }
  .person-name {
    font-weight: 700; font-size: 34px; letter-spacing: 0.5px;
  }
  .contact-row {
    display: flex; justify-content: flex-end; align-items: center;
    gap: 10px; font-size: 18px; line-height: 1.75;
  }
  .contact-rule {
    height: 1px; background: var(--rule); margin: 8px 0 8px auto; width: 300px;
  }
  .contact-details {
    position: absolute; right: 56px; top: 355px;
    background: var(--paper); padding: 8px 0 8px 24px;
  }
  .icon { width: 20px; height: 20px; flex: none; }

  /* Back */
  .back-brand {
    position: absolute; left: 0; right: 0; top: 50%;
    transform: translateY(-50%);
    display: flex; justify-content: center; align-items: center; gap: 20px;
  }
  .back-mark {
    width: 46px; height: 46px; border-radius: 50%; background: var(--paper);
  }
  .back-name {
    font-weight: 700; font-size: 44px; letter-spacing: 1px; color: var(--paper);
  }
</style>
</head>
<body>

<section class="card card-front" aria-label="Card front">
  <div class="brand">
    <div class="brand-name">THE STONEVALE CO.</div>
    <div class="brand-tagline">SCREENERS | CRUSHERS | STACKERS</div>
  </div>
  <div class="front-rule"></div>

  <div class="address">
    <svg class="icon" viewBox="0 0 20 20" aria-hidden="true">
      <circle cx="10" cy="10" r="10" fill="var(--olive)"/>
      <path d="M10 4.5a3.5 3.5 0 0 0-3.5 3.5c0 2.6 3.5 6.5 3.5 6.5s3.5-3.9 3.5-6.5A3.5 3.5 0 0 0 10 4.5z" fill="#fff"/>
      <circle cx="10" cy="8" r="1.3" fill="var(--olive)"/>
    </svg>
    <div>2210 - 48B Avenue<br>Ridgeford, alberta T0X 1A0</div>
  </div>

  <div class="band"></div>

  <div class="contact">
    <div class="person-name">DALE MORROW</div>
    <div class="contact-row">780.555.0142
      <svg class="icon" viewBox="0 0 20 20" aria-hidden="true"><circle cx="10" cy="10" r="10" fill="var(--olive)"/><rect x="7" y="4.5" width="6" height="11" rx="1" fill="#fff"/><rect x="8" y="6" width="4" height="6" fill="var(--olive)"/></svg>
    </div>
    <div class="contact-rule"></div>
  </div>

  <div class="contact-details">
    <div class="contact-row">780.555.0187
      <svg class="icon" viewBox="0 0 20 20" aria-hidden="true"><circle cx="10" cy="10" r="10" fill="var(--olive)"/><path d="M6.5 5.5l2 0 1 2.5-1.3 1a6 6 0 0 0 2.8 2.8l1-1.3 2.5 1v2a1 1 0 0 1-1 1A8 8 0 0 1 5.5 6.5a1 1 0 0 1 1-1z" fill="#fff"/></svg>
    </div>
    <div class="contact-row">780.555.0163
      <svg class="icon" viewBox="0 0 20 20" aria-hidden="true"><circle cx="10" cy="10" r="10" fill="var(--olive)"/><rect x="5" y="8" width="10" height="6" rx="1" fill="#fff"/><rect x="7" y="5" width="6" height="3" fill="#fff"/></svg>
    </div>
    <div class="contact-row">dale@stonevale.com
      <svg class="icon" viewBox="0 0 20 20" aria-hidden="true"><circle cx="10" cy="10" r="10" fill="var(--olive)"/><rect x="5" y="6.5" width="10" height="7" fill="#fff"/><path d="M5 6.5l5 4 5-4" fill="none" stroke="var(--olive)" stroke-width="1"/></svg>
    </div>
    <div class="contact-row">www.stonevale.ca
      <svg class="icon" viewBox="0 0 20 20" aria-hidden="true"><circle cx="10" cy="10" r="10" fill="var(--olive)"/><circle cx="10" cy="10" r="5" fill="none" stroke="#fff" stroke-width="1.3"/><path d="M5 10h10M10 5c-2 3-2 7 0 10M10 5c2 3 2 7 0 10" fill="none" stroke="#fff" stroke-width="1"/></svg>
    </div>
  </div>
</section>

<section class="card card-back" aria-label="Card back">
  <div class="back-brand">
    <div class="back-mark"></div>
    <div class="back-name">THE STONEVALE CO.</div>
  </div>
</section>

</body>
</html>
```